Recruitment talent email to send employers

We are a recruitment company specialising in STEM talent. We're after an eye catching email design to send our clients (ie employers) information about our top cadidates.

Target Market(s)

Employers

Requirements
Must have
• Must be clean/fresh looking, professional and concise

```html
<!DOCTYPE html>
<html lang="en">
<head>
<meta charset="utf-8">
<title>Nordvale Talent – Newsletter</title>
<link href="https://fonts.googleapis.com/css2?family=Montserrat:wght@500;700;800&family=Open+Sans:wght@400;600;700&display=swap" rel="stylesheet">
<style>
  :root{
    --page:#d9dad2;
    --card:#ffffff;
    --orange:#ef5a2a;
    --navy:#1f2b3c;
    --ink:#2e2e2e;
    --muted:#8a8a8a;
    --line:#e3e3e3;
    --footer:#2a2a2a;
    --photo-a:#c9ccd0;
    --photo-b:#8f9aa6;
  }
  *{box-sizing:border-box;margin:0;padding:0}
  html,body{width:1200px;height:2536px;overflow:hidden}
  body{background:var(--page);font-family:"Open Sans",Arial,sans-serif;color:var(--ink);position:relative}
  .abs{position:absolute}
  .preheader{top:66px;left:0;width:1200px;text-align:center;font-size:19px;color:var(--muted)}
  .preheader a{color:var(--orange);text-decoration:underline}
  .card{left:228px;top:120px;width:744px;height:2224px;background:var(--card);border-radius:12px;overflow:hidden;box-shadow:0 2px 10px rgba(0,0,0,.08)}
  .brand{display:flex;align-items:center;gap:14px}
  .brand-square{width:40px;height:40px;background:var(--navy)}
  .brand-name{font-family:"Montserrat",Arial,sans-serif;font-weight:700;font-size:26px;color:var(--navy);letter-spacing:1px}
  .header-brand{left:40px;top:38px}
  .date{right:40px;top:48px;font-size:22px;font-weight:600;color:var(--ink);display:flex;align-items:center;gap:10px}
  .hero{left:32px;top:148px;width:684px;height:412px;background:linear-gradient(120deg,var(--photo-b),var(--photo-a) 70%,#e8e6e2)}
  .hero-panel{left:0;top:0;width:330px;height:412px;background:rgba(31,43,60,.88)}
  .hero-title{left:32px;top:110px;width:300px;font-family:"Montserrat",Arial,sans-serif;font-weight:800;font-size:40px;line-height:48px;color:#fff}
  .section-title{font-family:"Montserrat",Arial,sans-serif;font-weight:800;font-size:34px;color:var(--ink);text-align:center;letter-spacing:1px}
  .section-title::after{content:"";display:block;width:60px;height:3px;background:var(--orange);margin:10px auto 0}
  .about-title{left:272px;top:600px;width:360px}
  .about-text{left:32px;top:680px;width:520px;font-size:15.5px;line-height:28px;color:#6b6b6b}
  .btn-outline{left:32px;top:892px;width:160px;height:48px;border:2px solid var(--orange);border-radius:24px;color:var(--orange);font-family:"Montserrat",Arial,sans-serif;font-weight:700;font-size:16px;display:flex;align-items:center;justify-content:center}
  .hex{left:586px;top:634px;width:138px;height:210px}
  .news-title{left:192px;top:1000px;width:360px}
  .news-card{border:2px solid var(--line);background:#fff}
  .news-main{left:32px;top:1048px;width:684px;height:292px}
  .news-main .thumb{left:18px;top:18px;width:244px;height:252px}
  .thumb{background:linear-gradient(135deg,#3b4454,#8b96a3 55%,#d4c8b8)}
  .meta{font-size:15px;font-weight:600;color:#555;display:flex;align-items:center;gap:8px}
  .headline{font-family:"Montserrat",Arial,sans-serif;font-weight:700;font-size:19px;line-height:26px;color:var(--ink)}
  .body{font-size:15.5px;line-height:26px;color:#6b6b6b}
  .read{font-family:"Montserrat",Arial,sans-serif;font-weight:700;font-size:18px;color:var(--orange)}
  .news-main .meta{left:282px;top:26px}
  .news-main .headline{left:282px;top:58px;width:380px}
  .news-main .body{left:282px;top:122px;width:380px}
  .news-main .read{left:282px;top:226px}
  .news-small{top:1360px;width:328px;height:328px}
  .news-left{left:32px}
  .news-right{left:388px}
  .news-small .thumb{left:30px;top:20px;width:268px;height:142px}
  .news-right .thumb{background:linear-gradient(135deg,#7fc5c2,#a9d9d3 60%,#e6ddd3)}
  .news-small .meta{left:30px;top:190px}
  .news-small .headline{left:30px;top:222px;width:270px;font-size:17px}
  .news-small .read{left:30px;top:262px}
  .btn-solid{left:256px;top:1720px;width:236px;height:56px;border-radius:28px;background:var(--orange);color:#fff;font-family:"Montserrat",Arial,sans-serif;font-weight:700;font-size:17px;display:flex;align-items:center;justify-content:center}
  .signup{left:32px;top:1820px;width:684px;height:140px;background:var(--orange);overflow:hidden}
  .signup svg{left:0;top:0}
  .signup-text{left:36px;top:40px;width:380px;font-family:"Montserrat",Arial,sans-serif;font-weight:700;font-size:19px;line-height:28px;color:#fff}
  .signup-field{left:476px;top:42px;width:188px;height:56px;border-radius:28px;background:var(--footer);color:#fff;font-size:14px;display:flex;flex-direction:column;align-items:center;justify-content:center;gap:2px}
  .footer{left:0;top:2000px;width:744px;height:224px;background:var(--footer)}
  .footer-brand{left:36px;top:50px}
  .footer-brand .brand-name{color:#fff}
  .footer-brand .brand-square{background:#fff}
  .copyright{left:36px;top:146px;font-size:17px;color:#d8d8d8}
  .follow{left:492px;top:74px;width:220px;text-align:center;font-size:19px;color:#e8e8e8}
  .socials{left:500px;top:124px;display:flex;gap:14px}
  .socials span{width:42px;height:42px;border:2px solid #fff;border-radius:50%}
</style>
</head>
<body>
  <p class="abs preheader">If you can not read this email | <a>click here</a></p>

  <main class="abs card">
    <header>
      <div class="abs brand header-brand"><span class="brand-square"></span><span class="brand-name">NORDVALE TALENT</span></div>
      <div class="abs date">
        <svg width="22" height="22" viewBox="0 0 22 22" aria-hidden="true"><rect x="2" y="4" width="18" height="16" rx="2" fill="none" stroke="#2e2e2e" stroke-width="2"/><line x1="2" y1="9" x2="20" y2="9" stroke="#2e2e2e" stroke-width="2"/><line x1="7" y1="1" x2="7" y2="6" stroke="#2e2e2e" stroke-width="2"/><line x1="15" y1="1" x2="15" y2="6" stroke="#2e2e2e" stroke-width="2"/></svg>
        31 Jan 2019
      </div>
    </header>

    <section class="abs hero" role="img" aria-label="Photo of a team meeting around a laptop in a bright office">
      <div class="abs hero-panel"></div>
      <h1 class="abs hero-title">We are a recruitment company specialising in STEM talent.</h1>
    </section>

    <section class="about">
      <h2 class="abs section-title about-title">ABOUT US</h2>
      <p class="abs about-text">Lorem ipsum dolor sit amet, consectetur adipiscing elit, sed do eiusmod tempor incididunt ut labore et dolore magna aliqua. Ut enim ad minim veniam, quis nostrud exercitation ullamco laboris nisi ut aliquip ex ea commodo consequat. Duis aute irure dolor in reprehenderit in voluptate velit esse cillum dolore eu fugiat nulla</p>
      <a class="abs btn-outline">Read More &gt;</a>
      <svg class="abs hex" viewBox="0 0 138 210" role="img" aria-label="Portrait photo of a smiling consultant">
        <defs><linearGradient id="hexfill" x1="0" y1="0" x2="1" y2="1"><stop offset="0" stop-color="#dfe7ea"/><stop offset="1" stop-color="#b9c6cc"/></linearGradient></defs>
        <polygon points="69,8 132,48 132,162 69,202 6,162 6,48" fill="none" stroke="#cfd8dc" stroke-width="3"/>
        <polygon points="69,20 122,54 122,156 69,190 16,156 16,54" fill="url(#hexfill)"/>
      </svg>
    </section>

    <section class="news">
      <h2 class="abs section-title news-title">LATEST NEWS</h2>

      <article class="abs news-card news-main">
        <div class="abs thumb" role="img" aria-label="Photo of a presenter beside a board of sticky notes"></div>
        <div class="abs meta"><svg width="16" height="16" viewBox="0 0 22 22" aria-hidden="true"><rect x="2" y="4" width="18" height="16" rx="2" fill="none" stroke="#555" stroke-width="2.5"/><line x1="2" y1="9" x2="20" y2="9" stroke="#555" stroke-width="2.5"/></svg>27 August 2018 | 04 : 1op. EST</div>
        <h3 class="abs headline">ullamco laboris nisi ut aliquip ex eachers state</h3>
        <p class="abs body">Lorem ipsum dolor sit amet, consectetur adipiscing elit, sed do eiusmod tempor incididunt ut labore et dolore magna aliqua. Ut enim ad ....</p>
        <a class="abs read">Read More &gt;</a>
      </article>

      <article class="abs news-card news-small news-left">
        <div class="abs thumb" role="img" aria-label="Photo of a person in a dark t-shirt"></div>
        <div class="abs meta"><svg width="16" height="16" viewBox="0 0 22 22" aria-hidden="true"><rect x="2" y="4" width="18" height="16" rx="2" fill="none" stroke="#555" stroke-width="2.5"/><line x1="2" y1="9" x2="20" y2="9" stroke="#555" stroke-width="2.5"/></svg>29 August 2018 | 04: 1o pa</div>
        <h3 class="abs headline">laboris nisi ut aliquip ex ea</h3>
        <a class="abs read">Read More &gt;</a>
      </article>

      <article class="abs news-card news-small news-right">
        <div class="abs thumb" role="img" aria-label="Photo of a smiling woman against a teal wall"></div>
        <div class="abs meta"><svg width="16" height="16" viewBox="0 0 22 22" aria-hidden="true"><rect x="2" y="4" width="18" height="16" rx="2" fill="none" stroke="#555" stroke-width="2.5"/><line x1="2" y1="9" x2="20" y2="9" stroke="#555" stroke-width="2.5"/></svg>29 August 2018 | 04: 1o pa</div>
        <h3 class="abs headline">laboris nisi ut aliquip ex ea</h3>
        <a class="abs read">Read More &gt;</a>
      </article>

      <a class="abs btn-solid">Watch More News &gt;</a>
    </section>

    <section class="abs signup">
      <svg class="abs" width="684" height="140" viewBox="0 0 684 140" aria-hidden="true">
        <polygon points="0,0 150,0 0,60" fill="#ffffff" opacity=".9"/>
        <polygon points="560,0 684,0 684,140 640,140" fill="#d9481d" opacity=".6"/>
      </svg>
      <p class="abs signup-text">Register our with your email address to get latest updates from us</p>
      <div class="abs signup-field">
        <svg width="18" height="13" viewBox="0 0 18 13" aria-hidden="true"><rect x="1" y="1" width="16" height="11" fill="none" stroke="#fff" stroke-width="1.6"/><polyline points="1,1 9,7 17,1" fill="none" stroke="#fff" stroke-width="1.6"/></svg>
        email address
      </div>
    </section>

    <footer class="abs footer">
      <div class="abs brand footer-brand"><span class="brand-square"></span><span class="brand-name">NORDVALE TALENT</span></div>
      <p class="abs copyright">Copyright © 1993-2018 Nordvale Ltd.</p>
      <p class="abs follow">Please Follow us on</p>
      <div class="abs socials"><span></span><span></span><span></span><span></span></div>
    </footer>
  </main>
</body>
</html>
```